Home Page Design

Please see design brief attached. Concept here: sketchboard[dot]io/file/qWm83LzpR7cvXuNtYa2KhE/Brindlemoor---Landing-Page?node-id=0%3A1&t=PKr92mvnQsD4xTcZ-1

Industry/Entity Type

Wedding

Number of Pages Required

1 page

Font styles to use
Serif
Sans Serif
Decorative
Script

Colors
A7469A
B969AE
D3A5CF
EDDBEB
F8F0F9
6B429C
8869AF
B7A5CE
E3DAEB
F3F0F8

Requirements
Must have
• Please see attached PDF
Nice to have
• Please see attached PDF
Should not have
• Please see attached PDF

```html
<!DOCTYPE html>
<html lang="en">
<head>
<meta charset="utf-8">
<title>Brindlemoor – Wedding Vendors</title>
<link rel="stylesheet" href="https://fonts.googleapis.com/css2?family=Playfair+Display:wght@400;500;600&family=Poppins:wght@400;500;600&display=swap">
<style>
:root{
  --plum:#6B2C70;
  --plum-deep:#5E2763;
  --band:#7B3F88;
  --orchid:#A7469A;
  --orchid-soft:#B969AE;
  --lilac:#D3A5CF;
  --blush:#F8F0F9;
  --ink:#2B2B2B;
  --text:#444;
  --white:#fff;
  --star:#F2B705;
}
*{margin:0;padding:0;box-sizing:border-box}
html,body{width:1200px;height:4011px;overflow:hidden;background:#fff}
body{position:relative;font-family:"Poppins",sans-serif;color:var(--text)}
.serif{font-family:"Playfair Display",serif}
.abs{position:absolute}

/* Header */
.site-header{position:absolute;left:0;top:0;width:1200px;height:90px;background:#fff;border-top:2px solid var(--plum)}
.brand{position:absolute;left:101px;top:28px;display:flex;align-items:center;gap:10px;font-family:"Playfair Display",serif;font-size:28px;color:var(--plum)}
.brand-dot{width:14px;height:14px;border-radius:50%;background:var(--orchid-soft)}
.main-nav a{position:absolute;top:36px;font-size:16px;color:#222;text-decoration:none}
.btn-vendor{position:absolute;left:900px;top:23px;width:200px;height:41px;border-radius:21px;background:var(--plum);color:#fff;font-size:16px;display:flex;align-items:center;justify-content:center}

/* Hero */
.hero{position:absolute;left:0;top:90px;width:1200px;height:626px;background:linear-gradient(180deg,#3d4a2e 0%,#5b5a3a 35%,#6a5643 65%,#3a3026 100%)}
.hero::after{content:"";position:absolute;inset:0;background:rgba(0,0,0,.28)}
.hero-title{position:absolute;left:0;width:1200px;top:440px;text-align:center;font-family:"Playfair Display",serif;font-size:40px;color:#fff;z-index:2}
.hero-sub{position:absolute;left:0;width:1200px;top:498px;text-align:center;font-size:16.5px;line-height:28px;color:#fff;z-index:2}
.search{position:absolute;left:324px;top:573px;width:551px;height:40px;background:#fff;border-radius:20px;display:flex;overflow:hidden;z-index:2;font-size:14px;color:#333}
.search .field{display:flex;align-items:center;justify-content:space-between;padding:0 22px 0 18px}
.search .f1{width:159px;border-right:1px solid #ccc;margin:8px 0;padding-left:18px}
.search .f2{width:268px;padding-left:46px}
.caret{width:0;height:0;border-left:5px solid transparent;border-right:5px solid transparent;border-top:6px solid #222}
.search .go{flex:1;background:var(--plum);color:#fff;display:flex;align-items:center;justify-content:center;font-size:15px}

/* Section titles */
.sec-title{position:absolute;left:0;width:1200px;text-align:center;font-family:"Playfair Display",serif;font-size:40px;color:#111}
.rule{position:absolute;left:570px;width:60px;height:2px;background:var(--plum)}

/* Vendors grid */
.vendor-grid{position:absolute;left:100px;top:869px;width:1000px;display:grid;grid-template-columns:repeat(4,242.5px);grid-auto-rows:236px;gap:7px 10px}
.vendor{position:relative;border-radius:6px;overflow:hidden}
.vendor span{position:absolute;left:14px;bottom:12px;font-family:"Playfair Display",serif;font-size:16px;color:#fff;padding-left:8px;border-left:3px solid var(--orchid-soft);line-height:16px}
.v1{background:linear-gradient(160deg,#6a5a45,#2d2620 60%,#8a8070)}
.v2{background:linear-gradient(160deg,#c9a48c,#e8cdbb 50%,#a98070)}
.v3{background:linear-gradient(180deg,#b9d0e0,#e7d8d8 55%,#e8b8c2)}
.v4{background:linear-gradient(160deg,#d76a7a,#9e2a3c 55%,#5d6a4a)}
.v5{background:linear-gradient(160deg,#b3123f,#3a1048 50%,#0e2a66)}
.v6{background:linear-gradient(180deg,#4d6a3a,#9a7a5a 55%,#c86a8a)}
.v7{background:linear-gradient(180deg,#ece6e2,#e3c9cf 50%,#f1ece8)}
.v8{background:linear-gradient(160deg,#5e6a55,#b9a392 50%,#3e4a3a)}

/* How it works */
.how{position:absolute;left:0;top:1441px;width:1200px;height:433px;background:linear-gradient(180deg,#7c3f89,#713a80)}
.how .sec-title{color:#fff;top:62px}
.how .rule{background:#fff;top:114px}
.step{position:absolute;top:164px;width:196px;height:196px}
.step-label{position:absolute;left:0;width:196px;top:112px;text-align:center;font-family:"Playfair Display",serif;font-size:15.5px;line-height:20px;color:#333}

/* About */
.about{position:absolute;left:0;top:1874px;width:1200px;height:532px;background:linear-gradient(90deg,#d8c6b2 0%,#e9dccb 30%,#cdb39a 55%,#6a5a4e 75%,#e2cfb8 100%)}
.about-card{position:absolute;left:103px;top:92px;width:426px;height:348px;background:#fff;border-radius:6px;padding:8px}
.about-card .inner{border:2px solid var(--plum);border-radius:6px;height:100%;padding:14px 20px 0 22px}
.about-card h2{font-family:"Playfair Display",serif;font-weight:400;font-size:38px;color:#111;line-height:48px}
.about-card p{font-size:16px;line-height:29.5px;color:#444;text-align:justify;margin-top:4px}
.btn-pill{display:inline-flex;align-items:center;justify-content:center;background:var(--plum);color:#fff;font-size:14px;font-weight:500;height:40px;width:152px;border-radius:20px;margin-top:12px}

/* Clients */
.clients{position:absolute;left:0;top:2406px;width:1200px;height:436px;background:var(--blush)}
.quote{position:absolute;left:190px;width:820px;top:161px;text-align:center;font-family:"Playfair Display",serif;font-style:italic;font-size:16.5px;line-height:31px;color:#444}
.client-name{position:absolute;left:0;width:1200px;top:275px;text-align:center;font-size:17px;font-weight:500;color:#222}
.stars{position:absolute;left:555px;top:305px}
.dots{position:absolute;left:555px;top:344px;display:flex;gap:10px}
.dots i{width:14px;height:14px;border-radius:50%;border:2px solid var(--plum);display:block}
.dots i.on{background:var(--plum)}

/* Blog */
.blog-card{position:absolute;top:3030px;width:313px;height:425px;background:#fff;box-shadow:0 2px 10px rgba(0,0,0,.08)}
.blog-img{height:210px}
.b1{background:linear-gradient(180deg,#5a3a2a,#c2a68c 50%,#6b4a34)}
.b2{background:linear-gradient(180deg,#5a78a8,#c9a070 55%,#5a3a2a)}
.b3{background:linear-gradient(160deg,#e8d4c6,#c79c86 55%,#f1e3d8)}
.blog-card h3{font-family:"Playfair Display",serif;font-weight:400;font-size:23px;line-height:27px;color:#222;padding:20px 16px 0;}
.blog-card p{font-size:13px;line-height:26.5px;color:#444;padding:13px 16px 0}
.blog-card a{display:inline-block;margin:6px 0 0 21px;font-size:15px;color:var(--plum);text-decoration:none;border-bottom:1.5px solid var(--plum);line-height:18px}

/* Footer */
.footer{position:absolute;left:0;top:3614px;width:1200px;height:397px;background:var(--plum)}
.signup{position:absolute;left:140px;top:3555px;width:918px;height:106px;background:#fff;border-radius:53px;box-shadow:0 2px 10px rgba(0,0,0,.1)}
.signup h3{position:absolute;left:42px;top:22px;font-family:"Playfair Display",serif;font-weight:500;font-size:26px;line-height:33px;color:#222}
.signup .form{position:absolute;left:327px;top:31px;width:551px;height:50px;border:1px solid #ddd;border-radius:25px;display:flex;font-size:14px;color:#555;overflow:hidden}
.signup .form span{display:flex;align-items:center;padding-left:20px}
.signup .name{width:165px;border-right:1px solid #999;margin:12px 0}
.signup .email{width:240px;padding-left:46px!important}
.signup .submit{flex:1;background:var(--plum);color:#fff;justify-content:center;padding:0!important;font-weight:600;font-size:18px;border-radius:25px}
.fcol{position:absolute;top:3715px}
.fcol h4{font-family:"Playfair Display",serif;font-weight:500;font-size:21px;color:#fff;margin-bottom:9px}
.fcol li{list-style:none;font-size:14.5px;line-height:31px;color:#fff}
.social{display:flex;gap:9px;margin-top:14px}
.social i{width:34px;height:34px;border-radius:50%;border:1.5px solid #fff;display:block}
.divider{position:absolute;left:100px;top:3938px;width:1000px;height:1px;background:rgba(255,255,255,.35)}
.copy{position:absolute;left:0;width:1200px;top:3961px;text-align:center;font-size:14px;color:#fff}
</style>
</head>
<body>

<header class="site-header">
  <div class="brand"><span class="brand-dot"></span>Brindlemoor</div>
  <nav class="main-nav">
    <a style="left:330px">Home</a>
    <a style="left:413px">Vendors</a>
    <a style="left:515px">Blog</a>
    <a style="left:587px">Contact Us</a>
    <a style="left:710px">Wedding Calculator</a>
  </nav>
  <div class="btn-vendor">sign up as a vendor</div>
</header>

<section class="hero" role="img" aria-label="Photo of a couple kissing outdoors while guests throw flower petals">
</section>
<h1 class="hero-title" style="font-weight:400">Are you looking for wedding vendors?</h1>
<p class="hero-sub">Lorem ipsum dolor sit amet, consectetur apiscing elit, sed do eiusmod tempor<br>incididunt ut labore et dolore magna aliqua.</p>
<div class="search">
  <div class="field f1">Location <span class="caret"></span></div>
  <div class="field f2">Wedding Venues <span class="caret"></span></div>
  <div class="go">Get Started</div>
</div>

<h2 class="sec-title" style="top:795px;font-weight:400">Find Your Dream Vendors</h2>
<div class="vendor-grid">
  <div class="vendor v1" role="img" aria-label="Photo of a reception hall under string lights"><span>Wedding Venue</span></div>
  <div class="vendor v2" role="img" aria-label="Photo of a bride having makeup applied"><span>Hair / Make Up</span></div>
  <div class="vendor v3" role="img" aria-label="Photo of a photographer shooting a couple"><span>Photography / Videography</span></div>
  <div class="vendor v4" role="img" aria-label="Photo of red roses"><span>Wedding Essentials</span></div>
  <div class="vendor v5" role="img" aria-label="Photo of headphones on a DJ mixer"><span>DJ / Entertainment</span></div>
  <div class="vendor v6" role="img" aria-label="Photo of a floral ceremony arch"><span>Decor / Florist</span></div>
  <div class="vendor v7" role="img" aria-label="Photo of a decorated banquet table"><span>Wedding Planner</span></div>
  <div class="vendor v8" role="img" aria-label="Photo of guests toasting with champagne"><span>Catering</span></div>
</div>

<section class="how">
  <h2 class="sec-title" style="font-weight:400">How It Works?</h2>
  <div class="rule"></div>

  <svg class="abs" style="left:0;top:0" width="1200" height="433" viewBox="0 0 1200 433">
    <g fill="none" stroke="#B969AE" stroke-width="3">
      <path d="M302 248 h18 M314 242 l7 6 -7 6"/>
      <path d="M565 248 h18 M577 242 l7 6 -7 6"/>
      <path d="M828 248 h18 M840 242 l7 6 -7 6"/>
    </g>
  </svg>

  <div class="step" style="left:104px">
    <svg width="196" height="196" viewBox="0 0 196 196">
      <circle cx="98" cy="98" r="94" fill="#fff" opacity=".18"/>
      <path d="M98 4 A94 94 0 0 1 98 192" fill="none" stroke="#C37ABA" stroke-width="9"/>
      <circle cx="98" cy="98" r="84" fill="#fff"/>
      <g fill="none" stroke="#333" stroke-width="2">
        <circle cx="98" cy="50" r="11"/><path d="M87 44 h22"/>
        <path d="M76 96 v-16 q0-14 22-14 q22 0 22 14 v16 z"/><path d="M90 66 l8 12 8-12"/>
      </g>
    </svg>
    <div class="step-label">Explore Vendors over<br>18+ Categories</div>
  </div>
  <div class="step" style="left:367px">
    <svg width="196" height="196" viewBox="0 0 196 196">
      <circle cx="98" cy="98" r="94" fill="#fff" opacity=".18"/>
      <path d="M98 4 A94 94 0 0 1 98 192" fill="none" stroke="#C37ABA" stroke-width="9"/>
      <circle cx="98" cy="98" r="84" fill="#fff"/>
      <g fill="none" stroke="#333" stroke-width="2">
        <rect x="80" y="36" width="36" height="50" rx="2"/><rect x="90" y="32" width="16" height="8"/>
        <path d="M86 52 l3 3 5-5 M98 53 h12 M86 64 l3 3 5-5 M98 65 h12 M86 76 l3 3 5-5"/>
        <path d="M104 82 l16-22 4 3 -16 22 -6 2z"/>
      </g>
    </svg>
    <div class="step-label">Send us your Desired<br>Requirements</div>
  </div>
  <div class="step" style="left:630px">
    <svg width="196" height="196" viewBox="0 0 196 196">
      <circle cx="98" cy="98" r="94" fill="#fff" opacity=".18"/>
      <path d="M98 4 A94 94 0 0 1 98 192" fill="none" stroke="#C37ABA" stroke-width="9"/>
      <circle cx="98" cy="98" r="84" fill="#fff"/>
      <g fill="none" stroke="#333" stroke-width="2.5">
        <path d="M72 40 h22 v22 q0 18 -16 26 l-4 -5 q10 -6 10 -17 h-12 z"/>
        <path d="M102 40 h22 v22 q0 18 -16 26 l-4 -5 q10 -6 10 -17 h-12 z"/>
      </g>
    </svg>
    <div class="step-label">Get a Free Quote and<br>Compare</div>
  </div>
  <div class="step" style="left:893px">
    <svg width="196" height="196" viewBox="0 0 196 196">
      <circle cx="98" cy="98" r="94" fill="#fff" opacity=".18"/>
      <path d="M98 4 A94 94 0 0 1 98 192" fill="none" stroke="#C37ABA" stroke-width="9"/>
      <circle cx="98" cy="98" r="84" fill="#fff"/>
      <g fill="none" stroke="#333" stroke-width="2">
        <path d="M60 62 l12 -14 10 8 M136 62 l-12 -14 -10 8"/>
        <path d="M72 48 l12 0 10 8 l10 -8 14 6 6 8"/>
        <path d="M82 56 l-10 8 20 20 q4 4 8 0 l20 -20"/>
        <path d="M86 72 l6 6 M92 66 l8 8 M98 62 l8 8"/>
      </g>
    </svg>
    <div class="step-label">Pick Best Deal and<br>Book Vendors</div>
  </div>
</section>

<section class="about" role="img" aria-label="Photo of a bride and groom sharing a dance in a decorated reception hall">
</section>
<div class="about-card" style="top:1966px">
  <div class="inner">
    <h2>About Us</h2>
    <p>At vero eos et accusamus et iusto odio dignissimos ducimus qui blanditiis praesentium voluptatum deleniti atque corrupti quos dolores et quas molestias excepturi sint occaecati cupiditate non provident, similique sunt in culpa qui officia deserunt mollitia animi, id est laborum et dolorum fuga. Et harum quidem</p>
    <span class="btn-pill">LEARN MORE</span>
  </div>
</div>

<section class="clients">
  <h2 class="sec-title" style="top:66px;font-size:46px;font-weight:400">Our Happy Clients</h2>
  <div class="rule" style="top:130px;width:80px;left:560px"></div>
  <p class="quote">At vero eos et accusamus et iusto odio dignissimos ducimus qui blanditiis praesentium voluptatum deleniti atque corrupti quos dolores et quas molestias excepturi sint occaecati cupiditate non provident, similique sunt in culpa qui officia deserunt mollitia animi, id est laborum et dolorum fuga.</p>
  <div class="client-name">Jonah Pryce</div>
  <svg class="stars" width="90" height="18" viewBox="0 0 90 18">
    <g fill="#F2B705">
      <path id="st" d="M9 0 l2.6 5.6 6.2.7 -4.6 4.2 1.3 6.1 -5.5-3.1 -5.5 3.1 1.3-6.1 -4.6-4.2 6.2-.7z"/>
      <use href="#st" x="18"/><use href="#st" x="36"/><use href="#st" x="54"/><use href="#st" x="72"/>
    </g>
  </svg>
  <div class="dots"><i></i><i></i><i class="on"></i><i></i></div>
</section>

<h2 class="sec-title" style="top:2940px;font-weight:400">Latest Blog</h2>
<div class="rule" style="top:3000px"></div>

<article class="blog-card" style="left:100px">
  <div class="blog-img b1" role="img" aria-label="Photo of a couple by tall windows"></div>
  <h3>The standard Lorem Ipsum ge, used since the 1500s</h3>
  <p>Lorem ipsum dolor sitmet, consectr adipiscing elit, sed do eiusmod tempor incididunt ut labore et dolore magna aliqua.</p>
  <a>LEARN MORE</a>
</article>
<article class="blog-card" style="left:444px">
  <div class="blog-img b2" role="img" aria-label="Photo of an outdoor dinner under paper lanterns"></div>
  <h3>The standard Lorem Ipsum ge, used since the 1500s</h3>
  <p>Lorem ipsum dolor sitmet, consectr adipiscing elit, sed do eiusmod tempor incididunt ut labore et dolore magna aliqua.</p>
  <a>LEARN MORE</a>
</article>
<article class="blog-card" style="left:787px">
  <div class="blog-img b3" role="img" aria-label="Photo of hands with an engagement ring"></div>
  <h3>The standard Lorem Ipsum ge, used since the 1500s</h3>
  <p>Lorem ipsum dolor sitmet, consectr adipiscing elit, sed do eiusmod tempor incididunt ut labore et dolore magna aliqua.</p>
  <a>LEARN MORE</a>
</article>

<footer class="footer"></footer>
<div class="signup">
  <h3>Sign Up To Get<br>Exclusive Information</h3>
  <div class="form">
    <span class="name">Full Name</span>
    <span class="email">Email Address</span>
    <span class="submit">Submit</span>
  </div>
</div>

<div class="fcol" style="left:100px">
  <h4>Quick Links</h4>
  <ul><li>About</li><li>Contact Us</li><li>Our Wedding Blogs</li><li>Customer FAQs</li><li>Vendor FAQs</li></ul>
</div>
<div class="fcol" style="left:358px">
  <h4>Other Links</h4>
  <ul><li>Faq</li><li>Terms Of Service</li><li>Contact</li></ul>
</div>
<div class="fcol" style="left:602px">
  <h4>Our Services</h4>
  <ul><li>Wedding Photography</li><li>Bridal Makeup</li><li>Bridal Mehndi</li><li>Bridal Outfits</li><li>Rental Transportation</li></ul>
</div>
<div class="fcol" style="left:881px">
  <h4>Planning &amp; Inspiration</h4>
  <ul><li>Search Vendors</li><li>Destination Weddings</li><li>Submit your Wedding</li></ul>
  <div class="social" aria-label="Social links"><i></i><i></i><i></i><i></i></div>
</div>
<div class="divider"></div>
<div class="copy">©Copyright ©2022 Brindlemoor. All Rights Reserved.</div>

</body>
</html>
```